Web re-design project for web software development agency

We need to re-design our existing website (www.tremondesign.co.uk), and are going to start using a shorter domain (www.tremon.com).
We have been in business for 8 years and it's time for an update.

We are based at Harrowmere Lodge (home of the code breakers). We specialise in writing software for the web. Over the years we have built up a healthy customer base and it is time to incorporate the features we build for our customers into our own site (e.g. social media).

We have a team of 8 talented developers with varied skills including: apps for mobile; complex server side software; front-end software; eCommerce software; specialised web based applications; integration software; hardware support; consultancy services. Our customers are diverse (e.g. banking; commerce; veterinary; R&D; health sector; law; accounting; film industry etc.).

Our current colour scheme is blue, white and green although we are not averse to moving away from these colours. We will also be dropping the DESIGN from our name and logo. Revised logo will be attached.

The site needs to be modern, sophisticated and leading edge. We want to show visitors to the site that we are a professional organisation.
Updates

Our logo in PSD format has been uploaded. Please drop the word DESIGN from the logo.

The deliverable for this project is a PSD (ideally we would like to see how the home page, portfolio page, resources page with mugshots, and forms are going to look).

Many thanks,
Tom

Please DO NOT include a Careers section 

We will also need a "meet our team" section with spaces for 10 photographs as well as some space underneath them so that we can add a short paragraph for each one of them.

Target Market(s)

Mainly large corporations needing bespoke web software, or generally complex projects (for anyone).

Industry/Entity Type

Software

Requirements
Must have
• We would like a home page designed that has the following elements on it:
- Show the new cookie compliance policy displayed probably in the top of the page (will disappear).
- A client Testimonial.
- Pricing icon.
- Social media Links.
- A Quote section in expand/collapse field as in (http://www.quorvix-online.co.uk/our-services.shtml)

We would also like a portfolio page that showcases our clients in an interesting way.

Finally, we would like a form design that we can use throughout the site (i.e. how should buttons, radio buttons, checkboxes, dropdowns, text areas etc. look)?
Nice to have
• A page that follows these guidelines:
http://www.pagelumo.com/the-anatomy-of-a-perfect-landing-page

Here are a few examples of sites in our sector that we like:
- http://www.mellow-craftwork.com/
- http://fendlix.co.uk/
- http://www.wexumo.com/services/web-development (nice contact us page)
- http://www.quorvix-online.co.uk/
- http://www.tasko.com/
- http://www.nethubro.co.uk/
Should not have
• No flash elemets. If anything, we will use html5.

```html
<!DOCTYPE html>
<html lang="en">
<head>
<meta charset="utf-8">
<title>Tremon – Web Application Development</title>
<link rel="stylesheet" href="https://fonts.googleapis.com/css2?family=Lato:wght@300;400;700;900&display=swap">
<style>
:root{
  --orange:#f7941d;
  --blue:#1d5a9c;
  --green:#8bbf2a;
  --ink:#1a1a1a;
  --night:#161616;
  --bar:#1e1e1e;
  --white:#fff;
}
*{box-sizing:border-box;margin:0;padding:0}
html,body{width:1062px;height:1200px;overflow:hidden}
body{position:relative;font-family:'Lato',sans-serif;color:var(--ink);background:var(--white)}
.abs{position:absolute}

.site-header{left:0;top:0;width:1062px;height:117px;background:linear-gradient(#e58a10,var(--orange) 60%,#fba531)}
.cookie-notice{left:0;top:0;width:1062px;height:22px;background:rgba(0,0,0,.55);color:var(--white);font-size:10px;display:flex;align-items:center;justify-content:center;gap:12px}
.cookie-notice button{font:700 9px 'Lato',sans-serif;background:var(--orange);color:var(--white);border:none;border-radius:2px;padding:2px 8px;text-transform:uppercase}
.brand{left:141px;top:44px;display:flex;align-items:center;gap:8px}
.brand-mark{width:24px;height:24px;background:var(--green)}
.brand-name{font-weight:900;font-size:28px;color:var(--blue);letter-spacing:.5px}
.main-nav{left:386px;top:74px;width:676px;height:29px;background:var(--bar);display:flex;align-items:center;padding-left:10px}
.main-nav a{color:var(--white);font-weight:900;font-size:11px;text-decoration:none;text-transform:uppercase;padding:0 10px 0 9px;border-left:2px solid var(--orange);line-height:14px;margin-right:22px}
.main-nav a:first-child{border-left:none}

.hero{left:0;top:117px;width:1062px;height:363px;background:linear-gradient(#eaeaea 0%,#a4a4a4 28%,#555 64%,#2d2d2d 65%,#333 100%)}
.hero-title{left:152px;top:33px;font-weight:900;font-size:23px;color:var(--white);text-transform:uppercase;text-shadow:0 1px 2px rgba(0,0,0,.4)}
.hero-copy{left:152px;top:108px;width:380px;color:var(--white)}
.hero-copy h2{font-weight:900;font-size:15px;line-height:20px;color:var(--orange);text-transform:uppercase;text-shadow:0 1px 1px rgba(0,0,0,.35)}
.hero-copy ul{list-style:none;margin:6px 0 0}
.hero-copy li{font-size:9.5px;text-transform:uppercase;line-height:20px}
.laptop{left:540px;top:77px}
.slider-dots{left:700px;top:302px;display:flex;gap:8px}
.slider-dots span{width:16px;height:16px;border-radius:50%;background:var(--orange);color:var(--white);font-size:10px;font-weight:900;display:flex;align-items:center;justify-content:center}
.slider-dots span.is-active{background:var(--white);color:var(--ink)}

.quote-toggle{left:141px;top:482px;font-size:22px;font-weight:300;display:flex;align-items:center;gap:8px}
.quote-toggle b{font-weight:900}
.pricing-link{left:300px;top:487px;display:flex;align-items:center;gap:5px;font-size:12px;font-weight:700;color:var(--ink)}
.share-bar{left:555px;top:488px;display:flex;gap:10px;font-size:10px}
.share-bar span{border:1px solid #bbb;border-radius:2px;padding:1px 5px;background:#f4f4f4;color:#335}
.share-bar span.count{background:var(--white);color:#333}

.section-band{height:28px;background:var(--orange)}
.section-title{font-size:23px;font-weight:300;line-height:28px}
.section-title b{font-weight:900}

.services{left:141px;top:555px;display:flex;gap:23px}
.service{width:83px;font-size:12px;line-height:14px}
.service .thumb{width:83px;height:82px;margin-bottom:16px}

.tech-grid{left:614px;top:548px;width:236px;display:grid;grid-template-columns:repeat(3,1fr);row-gap:22px;column-gap:4px;font-size:11px;font-weight:700}
.tech-grid span{display:flex;align-items:center;gap:4px}
.tech-grid i{width:10px;height:10px;border-radius:50%;background:var(--orange);flex:none}

.work-grid{left:143px;top:765px;display:grid;grid-template-columns:repeat(5,80px);gap:3px}
.work-tile{height:62px;border:1px solid #ccc;display:flex;align-items:center;justify-content:center;font-weight:900;font-size:11px;text-align:center}
.work-tile.light{background:var(--white);color:var(--blue)}
.work-tile.red{background:var(--white);color:#d8141b}
.work-tile.dark{background:#111;color:var(--white)}
.work-tile.navy{background:#1e4f8a;color:var(--white)}

.testimonial{left:632px;top:766px;width:270px;font-size:11px;line-height:18px;text-align:justify;color:#222}
.testimonial .mark{font-weight:900;font-size:34px;line-height:10px;vertical-align:-12px}

.follow-panel{left:0;top:943px;width:1062px;height:133px;background:linear-gradient(#e6e6e6,#f7f7f7)}
.panel-title{font-size:14px;font-weight:400;color:#444}
.panel-note{font-size:9px;color:#555}
.social-row{display:flex;gap:4px;align-items:center}
.social-row span{width:40px;height:40px;border-radius:4px;display:flex;align-items:center;justify-content:center;font-size:8px;font-weight:700;color:var(--white)}
.social-row span.counter{height:24px;border:1px solid #ccc;background:var(--white);color:#555;font-size:12px;font-weight:400;border-radius:2px}
.client-logos{display:grid;grid-template-columns:80px 90px;gap:8px 12px;font-size:11px;font-weight:700;color:#333}

.site-footer{left:0;top:1076px;width:1062px;height:124px;background:var(--night);color:var(--white)}
.badge{width:86px;height:32px;background:#dfe6ee;border:2px solid #999}
.legal{right:140px;top:26px;text-align:right;font-size:9px;font-weight:700}
.legal nav{font-size:14px;margin-top:6px}
</style>
</head>
<body>

<header class="site-header abs">
  <div class="cookie-notice abs">This site uses cookies to improve your experience. By continuing you agree to our cookie policy. <button type="button">OK</button></div>
  <div class="brand abs"><span class="brand-mark"></span><span class="brand-name">TREMON</span></div>
  <nav class="main-nav abs">
    <a href="#">Home</a><a href="#">About us</a><a href="#">Our services</a><a href="#">Technology</a><a href="#">Portfolio</a><a href="#">Contact us</a>
  </nav>
</header>

<section class="hero abs">
  <h1 class="hero-title abs">Our speciality : web application development and support</h1>
  <div class="hero-copy abs">
    <h2>Our passion is developing complex applications for the web that work for you and your business.</h2>
    <ul>
      <li>• We can turn your business processes into online web applications.</li>
      <li>• We can get your products or services selling online.</li>
      <li>• We can convert your site into one that you can maintain yourself.</li>
      <li>• We can help ensure your website is usable and standards compliant.</li>
    </ul>
  </div>
  <svg class="laptop abs" width="384" height="218" viewBox="0 0 384 218">
    <defs><linearGradient id="screen" x1="0" y1="0" x2="0" y2="1"><stop offset="0" stop-color="#d8d8d8"/><stop offset=".5" stop-color="#555"/><stop offset="1" stop-color="#cfe4f2"/></linearGradient></defs>
    <rect x="12" y="0" width="360" height="196" rx="8" fill="#222"/>
    <rect x="20" y="8" width="344" height="180" fill="url(#screen)" role="img" aria-label="Screenshot of a web design showcase page"/>
    <path d="M0 196 H384 L372 210 H12 Z" fill="#c9c9c9"/>
  </svg>
  <div class="slider-dots abs"><span class="is-active">1</span><span>2</span><span>3</span></div>
</section>

<div class="quote-toggle abs">
  <svg width="18" height="12" viewBox="0 0 18 12"><path d="M2 10 L9 3 L16 10" stroke="#111" stroke-width="3" fill="none"/></svg>
  <span>Get <b>Qoute</b></span>
</div>
<a class="pricing-link abs" href="#">
  <svg width="18" height="18" viewBox="0 0 18 18"><path d="M2 2 H9 L16 9 L9 16 L2 9 Z" fill="var(--orange)"/><circle cx="6" cy="6" r="1.6" fill="#fff"/></svg>
  Pricing
</a>
<div class="share-bar abs">
  <span>Like</span><span class="count">2.4k</span><span>Share</span><span class="count">2.5K</span><span>Chirp</span><span class="count">448</span><span>+1</span><span class="count">336</span><span>★ Rate</span>
</div>

<div class="section-band abs" style="left:0;top:510px;width:590px"></div>
<div class="section-band abs" style="left:614px;top:510px;width:448px"></div>
<h2 class="section-title abs" style="left:141px;top:510px">Our <b>Services</b></h2>
<h2 class="section-title abs" style="left:628px;top:509px">Our <b>Technology</b></h2>

<div class="services abs">
  <div class="service"><div class="thumb" role="img" aria-label="Networked computers around a globe" style="background:linear-gradient(135deg,#dbeafb,#2f7fd1)"></div>Development</div>
  <div class="service"><div class="thumb" role="img" aria-label="Hand sketching a flowchart" style="background:linear-gradient(135deg,#f4f4f4,#b9b9b9)"></div>Project Management</div>
  <div class="service"><div class="thumb" role="img" aria-label="Support team members" style="background:linear-gradient(135deg,#e9e9e9,#6b6b6b)"></div></div>
  <div class="service"><div class="thumb" role="img" aria-label="Keyboard key labelled support" style="background:linear-gradient(135deg,#eaf4fb,#5aa2cf)"></div>Ongoing Support</div>
</div>

<div class="tech-grid abs">
  <span><i></i>Tuxora</span><span><i></i>Phyla</span><span><i></i>Dolphquery</span>
  <span><i></i>Explorix</span><span><i></i>Compasso</span><span><i></i>Vulpina</span>
  <span><i></i>Arietta</span><span><i></i>Webstand</span>
</div>

<div class="section-band abs" style="left:0;top:719px;width:590px"></div>
<div class="section-band abs" style="left:614px;top:719px;width:448px"></div>
<h2 class="section-title abs" style="left:141px;top:719px">Our <b>Work</b></h2>
<h2 class="section-title abs" style="left:628px;top:718px">Client <b>Testimonials</b></h2>

<div class="work-grid abs">
  <div class="work-tile light">Halvern &amp; Reed</div>
  <div class="work-tile red">K&amp;P</div>
  <div class="work-tile navy">Solvista</div>
  <div class="work-tile light">Halvern &amp; Reed</div>
  <div class="work-tile red">K&amp;P</div>
  <div class="work-tile dark">Voltrex</div>
  <div class="work-tile dark">Carrow</div>
  <div class="work-tile dark">Orbisound</div>
  <div class="work-tile dark">Voltrex</div>
  <div class="work-tile dark">Carrow</div>
</div>

<blockquote class="testimonial abs">
  <span class="mark">“</span> When we asked Nethubro to join the project to re-develop our website, two major web agencies had already backed out after doing initial work as they believed the task was too demanding. Nethubro grasped the nettle, delivering the website before the deadline. This was due not only to great technical skills but also excellent communication, development and project management. <span class="mark">”</span>
</blockquote>

<section class="follow-panel abs">
  <h3 class="panel-title abs" style="left:143px;top:12px">Follow us</h3>
  <p class="panel-note abs" style="left:143px;top:38px">Follow our Kinloop, Chirply, Workvine and blog sites...</p>
  <div class="social-row abs" style="left:143px;top:66px">
    <span style="background:#3b5b9a">Kinloop</span><span style="background:#4fb3d9">Chirply</span><span style="background:#1a77a8">Workvine</span><span style="background:#f08a1c">Blog</span>
    <span class="counter">0</span>
  </div>
  <h3 class="panel-title abs" style="left:628px;top:12px;font-size:13px">Client Client</h3>
  <div class="client-logos abs" style="left:628px;top:52px">
    <span>Lumavia</span><span>Aurumvault</span><span>Veterion</span><span style="color:#b71c1c">Rattlebox Records</span>
  </div>
</section>

<footer class="site-footer abs">
  <div class="abs" style="left:143px;top:28px;display:flex;gap:10px"><span class="badge"></span><span class="badge"></span></div>
  <div class="legal abs">
    <p>© Tremon Ltd. 2012 Registered in England &amp; Wales Number: 04829317.</p>
    <nav>sitemap &nbsp;|&nbsp; login</nav>
  </div>
</footer>

</body>
</html>
```